Marisol Penhaw tutoring Advertising package - flyers, posters, business card and logo

I am looking for a flyer design for my tutoring business, it needs to explain what tutoring services I offer, how much I charge, why my services are worthwhile, it should include some photos of me and the tutoring centre,

It needs to include my phone number and my website. It should quote from some of the testimonials I have received from parents and children.

My website is www.marisolpenhaw.example My Facebook page can be found at https://www.facebook.example/marisolpenhawtutoring These pages include a range of photos and quotes that you can use.

I am not sure about the colours and designs that I would like, that's why I'm using Artflock!
I'm looking to appeal to parents inform them of my skills and experience.

I'm charging $45 for sessions of an hour and 15 minutes. 2 sessions per week will cost $80. I tutor Monday to Friday afternoons and evenings along with all day Saturdays. The assessment is free.

I tutor children from K-9 in English and Maths. I'm mainly aiming at parents whose children are struggling a little bit at school although I can help children who are doing well too.
I am highly skilled at helping children who can't read, I have a comprehensive program, the Calder program, that specifically teaches children the skills they need to read fluently and successfully.

Similarly I have had a lot of experience at helping children improve their Maths skills. I am well resourced with a wide range of hands on resources, paper resources and electronic resources.

Children will get better NAPLAN results if I tutor them (NAPLAN is the national series of tests in Australia).

I'm after a DL double sided flyer, and an A4 flyer. I'm also looking for two A2 posters and two A3 posters. Finally, I want a business card too. I don't have a logo for the business and I'd love to have one!

Target Market(s)

Parents of school aged children

Industry/Entity Type

Education

Colors

Designer to choose colors to be used in the design.

Requirements
Must have
• my name, my photo, length and cost of my sessions, email and phone contact details. Subjects and age ranges that I teach, times that I tutor. Website and/or Facebook page references. Quotes from Testimonials
Nice to have
• The A2 and A3 posters should complement each other.

```html
<!DOCTYPE html>
<html lang="en">
<head>
<meta charset="utf-8">
<title>Marisol Penhaw – Private Tutor Flyer</title>
<link rel="stylesheet" href="https://fonts.googleapis.com/css2?family=Libre+Baskerville:wght@700&family=Lato:ital,wght@0,400;0,700;0,900;1,700&display=swap">
<style>
  :root {
    --green: #0f8a4f;
    --green-dark: #0b7340;
    --yellow: #f8c600;
    --gold: #f5c518;
    --ink: #2f2f2f;
    --charcoal: #3a3a3a;
    --paper: #ffffff;
    --paper-shade: #ececec;
    --serif: "Libre Baskerville", Georgia, serif;
    --sans: "Lato", Arial, sans-serif;
  }
  * { box-sizing: border-box; margin: 0; padding: 0; }
  html, body { width: 900px; height: 1200px; overflow: hidden; }
  body { background: #f2f2f2; font-family: var(--sans); color: var(--ink); }

  .flyer {
    position: relative; width: 900px; height: 1200px; overflow: hidden;
    background: linear-gradient(180deg, var(--paper) 55%, var(--paper-shade) 100%);
  }

  .portrait {
    position: absolute; left: 0; top: 0; width: 441px; height: 512px;
    background: linear-gradient(160deg, #dcd9d2 0%, #b9a48a 45%, #7d5f45 75%, #9fc3d6 100%);
  }
  .portrait-band {
    position: absolute; left: 0; top: 512px; width: 441px; height: 36px;
    background: var(--charcoal);
  }

  .intro {
    position: absolute; left: 441px; top: 0; width: 459px; height: 590px;
    background: var(--yellow);
  }
  .intro-text {
    position: absolute; left: 37px; top: 196px; width: 382px;
    font-size: 15px; line-height: 19px; color: #2a2a2a; text-align: justify;
  }
  .intro-text p + p { margin-top: 19px; }

  .title-box {
    position: absolute; left: 421px; top: 36px; width: 479px; height: 136px;
    background: var(--green); text-align: center; color: var(--paper);
  }
  .title-name {
    font-family: var(--serif); font-weight: 700; color: var(--gold);
    font-size: 38px; letter-spacing: 0.5px; margin-top: 22px; line-height: 48px; white-space: nowrap;
  }
  .title-rule {
    width: 380px; height: 2px; margin: 6px auto 0;
    background: linear-gradient(90deg, transparent, var(--gold), transparent);
  }
  .title-role { font-family: var(--sans); font-weight: 700; font-size: 29px; margin-top: 10px; letter-spacing: 0.5px; }

  .testimonials {
    position: absolute; left: 35px; top: 486px; width: 355px; height: 424px;
    background: var(--green); color: var(--paper); padding: 24px 20px 0 20px;
  }
  .testimonials::before {
    content: ""; position: absolute; left: -12px; top: 0;
    border-right: 12px solid #1d1d1d; border-top: 26px solid transparent;
  }
  .section-heading {
    font-family: var(--serif); font-weight: 700; color: var(--gold);
    font-size: 22px; text-align: center; letter-spacing: 0.5px;
  }
  .heading-rule { width: 250px; height: 2px; margin: 4px auto 14px; background: linear-gradient(90deg, transparent, var(--gold), transparent); }
  .quote { font-size: 15px; line-height: 19px; text-align: justify; }
  .quote + .quote { margin-top: 20px; }
  .quote-author { display: block; color: var(--gold); font-weight: 700; font-style: italic; font-size: 14.5px; text-align: left; }

  .headline {
    position: absolute; left: 420px; top: 602px; width: 480px; text-align: center;
  }
  .headline-main { font-family: var(--serif); font-weight: 700; color: var(--green); font-size: 36px; line-height: 44px; white-space: nowrap; }
  .headline-sub { font-family: var(--serif); font-weight: 700; color: var(--charcoal); font-size: 20px; line-height: 24px; white-space: nowrap; }
  .headline-sub .small { color: var(--green); font-size: 13px; }
  .headline-note { font-family: var(--serif); font-weight: 700; color: var(--ink); font-size: 16px; line-height: 22px; white-space: nowrap; }

  .services-tab {
    position: absolute; left: 682px; top: 706px; width: 218px; height: 38px;
  }
  .services-tab span {
    position: absolute; right: 0; width: 150px; top: 7px; text-align: center;
    font-family: var(--serif); font-weight: 700; color: var(--gold); font-size: 20px;
  }

  .services {
    position: absolute; left: 420px; top: 758px; width: 455px; list-style: none;
  }
  .services li {
    position: relative; padding-right: 35px; text-align: right;
    font-size: 15px; line-height: 19px; color: #333;
  }
  .services li + li { margin-top: 18px; }
  .services li::after {
    content: ""; position: absolute; right: 2px; top: 6px; width: 9px; height: 9px;
    border-radius: 50%; background: var(--green);
  }

  .sessions { position: absolute; left: 35px; top: 926px; width: 355px; text-align: center; }
  .sessions-title { font-family: var(--serif); font-weight: 700; font-size: 22px; line-height: 26px; color: var(--charcoal); }
  .sessions-title .accent { color: var(--green); }
  .sessions-rule { width: 270px; height: 2px; margin: 4px auto 6px; background: linear-gradient(90deg, transparent, var(--green), transparent); }
  .sessions-days { font-size: 19px; line-height: 24px; color: #333; }
  .sessions-days .sep { color: var(--green); font-weight: 700; padding: 0 3px; }

  .footer-shapes { position: absolute; left: 0; top: 1070px; width: 900px; height: 130px; }

  .price { position: absolute; left: 40px; top: 1112px; width: 340px; text-align: center; }
  .price-line { font-family: var(--serif); font-weight: 700; font-size: 24px; color: var(--green); white-space: nowrap; }
  .price-line .amount { font-family: var(--sans); font-weight: 900; color: var(--charcoal); font-size: 28px; }
  .price-unit { font-weight: 900; font-size: 18px; letter-spacing: 6px; color: var(--charcoal); margin-top: 2px; }

  .contact {
    position: absolute; left: 470px; top: 1144px; width: 410px;
    display: flex; justify-content: flex-end; gap: 22px; color: var(--paper);
    font-weight: 700; font-size: 17px; align-items: center; white-space: nowrap;
  }
  .contact-item { display: flex; align-items: center; gap: 6px; white-space: nowrap; }
  .contact-item svg { width: 15px; height: 15px; flex: none; }
</style>
</head>
<body>
<main class="flyer">
  <div class="portrait" role="img" aria-label="Photo of Marisol Penhaw smiling at a desk in the tutoring room, bookshelves and a wall map behind"></div>
  <div class="portrait-band"></div>

  <section class="intro">
    <div class="intro-text">
      <p>Hi, I’m Marisol Penhaw. I’m 43 years old and this is my 25th year of tutoring K-8 children.</p>
      <p>Is your child struggling at school? Would you like to see your child succeed at school? Do you want them to enjoy learning?</p>
      <p>It can happen. I am a teacher, I am a mother, I am a lifelong learner and I can help your child grow.</p>
      <p>Your child will experience success and that is strongly motivating.</p>
      <p>I use the Calder Method for reading. It works because it is clear, logical and ensures that young readers experience success. It is based upon the fact that English is an alphabetic language and has been developed by working with children!</p>
    </div>
  </section>

  <header class="title-box">
    <h1 class="title-name">MARISOL PENHAW</h1>
    <div class="title-rule"></div>
    <p class="title-role">PRIVATE TUTOR</p>
  </header>

  <section class="testimonials">
    <h2 class="section-heading">TESTIMONIALS</h2>
    <div class="heading-rule"></div>
    <p class="quote">"Marisol is patient, funny, professional, knowledgeable and above all has a real interest in seeing her students improve and excel. "<span class="quote-author">Renata Oduya, parent</span></p>
    <p class="quote">“ She is smart and cool and the best teacher in the world!”<span class="quote-author">Tilly Oduya, student</span></p>
    <p class="quote">Marisol is a highly skilled, effective teacher who has an excellent rapport with her students. I have taught with her over the years since 1996 and found her to be a motivated, caring teacher who gets the best out of her students. I have no hesitation in recommending her to achieve success with your child.<span class="quote-author">Gareth Voss, teacher and tutor</span></p>
  </section>

  <section class="headline">
    <h2 class="headline-main">CHILDREN WILL GET</h2>
    <p class="headline-sub"><span class="small">BETTER</span> NAPLAN RESULTS <span class="small">IF I TUTOR THEM</span></p>
    <p class="headline-note">(NAPLAN is the national series of tests in Australia)</p>
  </section>

  <div class="services-tab">
    <svg width="218" height="38" viewBox="0 0 218 38" aria-hidden="true"><polygon points="38,0 218,0 218,38 0,38" fill="var(--green)"/></svg>
    <span>SERVICES</span>
  </div>

  <ul class="services">
    <li>I help children learn Maths in a clear, logical manner. I help them learn simple, effective techniques that will develop their speed and accuracy in Maths. I use technology and hands on resources to develop their understanding of concepts.</li>
    <li>I know how to use technology with your children. I use professional, quality programs that are engaging and useful. I provide fast computers and wireless Internet when to support your child’s learning.</li>
    <li>I am a skilled and experienced teacher. I enjoy working with children and they respond well to me. I love learning and it’s natural for me to share that love with children.</li>
    <li>I offer a practical Science course that engages children and develops their understanding and knowledge of Science through conducting and analysing experiments.</li>
  </ul>

  <section class="sessions">
    <h2 class="sessions-title">CURRENT SESSIONS<br><span class="accent">AVAILABLE ON</span></h2>
    <div class="sessions-rule"></div>
    <p class="sessions-days">Monday<span class="sep">|</span>Wednesday<span class="sep">|</span>Thursday<br>Friday<span class="sep">|</span>Saturday</p>
  </section>

  <svg class="footer-shapes" viewBox="0 0 900 130" aria-hidden="true">
    <polygon points="0,0 440,0 510,130 0,130" fill="var(--yellow)"/>
    <polygon points="400,40 900,40 900,130 460,130" fill="var(--green)"/>
  </svg>

  <div class="price">
    <p class="price-line"><span class="amount">$45</span> FOR SESSIONS</p>
    <p class="price-unit">PER HOUR</p>
  </div>

  <div class="contact">
    <span class="contact-item">
      <svg viewBox="0 0 16 16" aria-hidden="true"><path d="M4 1.5 6.3 4.2 5 6c.9 2 2.6 3.8 4.8 4.9l1.8-1.3 2.9 2.3-1.4 2.4C7.8 14.1 1.8 8.4 1.6 2.9Z" fill="var(--yellow)"/></svg>
      0400 555 019
    </span>
    <span class="contact-item">
      <svg viewBox="0 0 16 16" aria-hidden="true"><g fill="none" stroke="var(--yellow)" stroke-width="1.5"><circle cx="8" cy="8" r="6.5"/><ellipse cx="8" cy="8" rx="2.8" ry="6.5"/><line x1="1.5" y1="8" x2="14.5" y2="8"/></g></svg>
      www.marisolpenhaw.example
    </span>
  </div>
</main>
</body>
</html>
```